Granite Ridge Response Business Card

Side 1: Granite Ridge Response Logo (logo without Maltese cross) with industrial rope rescue related theme. Our company services - TRAINING - Fire Training, Confined Space Rescue Training, Rope Rescue training, Hazmat Training, Incident Command, EMS, Pump Operations Training. Website - graniteridgeresponse.example.
Side 2: Granite Ridge Response Fire Department Logo (logo with Maltese cross) with Firefighter related theme. Company (division) services - FIELD SERVICES - Fire Department, Stand-by Rescue, Safety, EMS, Planning. "Supporting the Emergency Response Community Since 1967"

Add contact information wherever it makes since (Name, Email, Phone).
I would like it to represent the Granite Ridge Response Fire Department Logo as a division not as a separate entity without saying it, possibly by depicting it in the background of Side 2 instead of being a standalone picture like the logo on Side 1.

```html
<!DOCTYPE html>
<html lang="en">
<head>
<meta charset="UTF-8">
<title>Granite Ridge Response Business Card</title>
<link rel="stylesheet" href="https://fonts.googleapis.com/css2?family=Poppins:wght@400;500;600;700&display=swap">
<style>
  :root {
    --stage: #2d2d2d;
    --card: #000000;
    --red: #ff0a0a;
    --white: #ffffff;
    --grey: #cfcfcf;
  }
  * { margin: 0; padding: 0; box-sizing: border-box; }
  html, body { width: 1200px; height: 1015px; overflow: hidden; }
  body {
    background: var(--stage);
    font-family: "Poppins", sans-serif;
    display: flex;
    flex-direction: column;
    align-items: center;
    justify-content: center;
    gap: 56px;
  }
  .card {
    position: relative;
    width: 620px;
    height: 354px;
    background: var(--card);
    box-shadow: 0 12px 30px rgba(0,0,0,.45);
    display: flex;
    flex-direction: column;
    align-items: center;
    justify-content: center;
    text-align: center;
    overflow: hidden;
  }
  .card::after {
    content: "";
    position: absolute;
    left: 0; right: 0; bottom: 0;
    height: 8px;
    background: var(--red);
  }
  .bullet { color: var(--red); margin: 0 6px; }
  .bullet-white { color: var(--white); margin: 0 8px; }

  /* Side 1 */
  .brand {
    display: flex;
    align-items: center;
    gap: 12px;
    color: var(--red);
    font-weight: 700;
    font-size: 26px;
    letter-spacing: 1px;
    text-transform: uppercase;
    margin-bottom: 8px;
  }
  .brand-mark { width: 14px; height: 14px; background: var(--red); border-radius: 50%; }
  .brand-rule { width: 260px; height: 2px; background: var(--red); margin-bottom: 26px; }
  .services {
    color: var(--grey);
    font-size: 13.5px;
    font-weight: 500;
    letter-spacing: .6px;
    text-transform: uppercase;
    line-height: 1.75;
  }
  .website {
    margin-top: 22px;
    font-size: 14px;
    color: var(--white);
    letter-spacing: .5px;
  }
  .website .domain { color: var(--red); }

  /* Side 2 */
  .person-name { color: var(--red); font-weight: 700; font-size: 22px; }
  .name-rule { width: 60px; height: 1px; background: var(--white); margin: 8px 0 10px; }
  .contact { color: var(--white); font-size: 14px; line-height: 1.6; }
  .field-services {
    margin-top: 26px;
    color: var(--red);
    font-size: 19px;
    font-weight: 500;
    text-transform: uppercase;
    line-height: 1.35;
  }
  .tagline { margin-top: 28px; color: var(--white); font-size: 13.5px; font-weight: 500; }
</style>
</head>
<body>
  <section class="card card-training">
    <div class="brand"><span class="brand-mark"></span>Granite Ridge Response</div>
    <div class="brand-rule"></div>
    <p class="services">
      Fire Training<span class="bullet">&bull;</span>Confined Space Rescue Training<br>
      Rope Rescue Training<span class="bullet">&bull;</span>Hazmat Training<br>
      Incident Command<span class="bullet">&bull;</span>EMS<span class="bullet">&bull;</span>Pump Operations Training
    </p>
    <p class="website">www.<span class="domain">graniteridgeresponse</span>.example</p>
  </section>

  <section class="card card-field">
    <h1 class="person-name">Marcus Hale</h1>
    <div class="name-rule"></div>
    <p class="contact">044-555 018 204<br>crew@graniteridgeresponse.example</p>
    <p class="field-services">
      Fire Department<span class="bullet-white">&bull;</span>Stand-by Rescue<br>
      Safety<span class="bullet-white">&bull;</span>EMS<span class="bullet-white">&bull;</span>Planning
    </p>
    <p class="tagline">Supporting the Emergency Response Community Since 1967</p>
  </section>
</body>
</html>
```